family chiropractic health care team needs a modern business card design

Healthcare office with Chiropractors, Physiotherapists, Massage therapists and possibly other practitioners in the future. This is a friendly family office with patients of all ages (and lots of kids) that just moved into a new larger modern office.
Look at the website for photos of the office.
Design for the front and back of a business card required.
Text for the front:
Office logo and name of the office:
Bright Path Wellness Centre
Name of current Practitioner:
Dr. Marten Quovel B.Sc., D.C. Chiropractor
(But please include options to swap out name and title for other practitioners )

address:
218 Farrow Gate
Etobicoke ON.
K2J 6P4
Phone: 416-872-0196 (PATH)
Web site and email:
www.brightpathwellnesscentre.example
brightpathchiro@mailbox.example

2 versions of the back of the card:
1. text below
2. appointment schedule card

Text on back of card:
Chiropractic Card text on back of the card:
There is more to chiropractic than the relief of headaches and back pain! Our primary focus is the integrity of your nerve system, which controls and regulates every cell and tissue of your body. The moving bones of the spinal column can impair this vital communication link between your brain and body. We help improve the function and structure of your spine, reducing nerve system compromise. The result?
Even non-spinal related health problems can show improvement
without drugs
without surgery
regardless of age
for over a century
naturally

Appointment Card info For Back:
Please integrate design elements from the front of the card into an appointment card format.
M Tu W Th F Sat (and a line for writing on beside each one)

```html
<!DOCTYPE html>
<html lang="en">
<head>
<meta charset="utf-8">
<title>Bright Path Wellness Centre – Business Card</title>
<link rel="stylesheet" href="https://fonts.googleapis.com/css2?family=Cinzel:wght@400&family=Arimo:wght@400;700&display=swap">
<style>
  :root {
    --backdrop: #2b2b2b;
    --card-dark: #343434;
    --card-light: #ffffff;
    --green: #7dbf3c;
    --grey-text: #5a5a5a;
    --wordmark-dark: #8a8a8a;
    --light-text: #f2f2f2;
    --rule: #d4d4d4;
  }
  * { box-sizing: border-box; margin: 0; padding: 0; }
  html, body { width: 1200px; height: 689px; overflow: hidden; }
  body {
    background: var(--backdrop);
    display: flex;
    align-items: center;
    justify-content: center;
    gap: 40px;
    font-family: "Arimo", Arial, sans-serif;
  }
  .card {
    position: relative;
    width: 540px;
    height: 308px;
    border-radius: 18px;
    border-bottom: 4px solid var(--green);
    box-shadow: 0 10px 30px rgba(0,0,0,.45);
    overflow: hidden;
  }

  /* Plain name set in the card's text font */
  .wordmark {
    font-family: "Arimo", Arial, sans-serif;
    font-weight: 700;
    font-size: 22px;
    line-height: 1.2;
    display: flex;
    align-items: center;
    gap: 9px;
  }
  .wordmark .dot { width: 12px; height: 12px; border-radius: 50%; flex: none; }

  /* Back */
  .card-back { background: var(--card-dark); color: var(--light-text); padding: 30px 40px 0; }
  .card-back .wordmark { color: var(--wordmark-dark); justify-content: center; }
  .card-back .wordmark .dot { background: var(--wordmark-dark); }
  .mission { margin-top: 20px; font-size: 11.5px; line-height: 1.42; text-align: center; }
  .highlight { margin-top: 14px; color: var(--green); font-weight: 700; font-size: 13.5px; text-align: center; }
  .benefits {
    list-style: none;
    margin: 7px auto 0;
    display: flex; flex-wrap: wrap; justify-content: center;
    gap: 4px 16px;
    max-width: 400px;
    font-size: 12px;
  }
  .benefits li { display: flex; align-items: center; gap: 5px; }
  .tick { width: 12px; height: 12px; flex: none; }

  /* Front */
  .card-front { background: var(--card-light); }
  .card-front .wordmark {
    position: absolute; right: 34px; top: 42px;
    color: var(--green);
  }
  .card-front .wordmark .dot { background: var(--green); }
  .divider { position: absolute; left: 34px; right: 34px; top: 104px; height: 1px; background: var(--rule); }
  .address {
    position: absolute; right: 34px; top: 116px;
    color: var(--grey-text); font-size: 12px; line-height: 1.35; text-align: right;
    font-style: normal;
  }
  .practitioner { position: absolute; left: 34px; top: 166px; }
  .practitioner .name {
    font-family: "Cinzel", Georgia, serif; color: var(--green);
    font-size: 22px; font-weight: 400; letter-spacing: .02em; line-height: 1.1;
  }
  .practitioner .creds { font-family: "Cinzel", Georgia, serif; color: var(--green); font-size: 12px; margin-top: 3px; }
  .practitioner .title { color: var(--grey-text); font-size: 12px; margin-top: 3px; }
  .contacts { position: absolute; left: 34px; bottom: 22px; list-style: none; color: #3a3a3a; font-size: 12px; }
  .contacts li { display: flex; align-items: center; gap: 8px; line-height: 1.5; }
  .contacts svg { width: 11px; height: 11px; flex: none; fill: var(--green); }
</style>
</head>
<body>

<section class="card card-back" aria-label="Card back">
  <div class="wordmark"><span class="dot"></span>Bright Path Wellness Centre</div>
  <p class="mission">There is more to chiropractic than the relief of headaches and back pain! Our primary focus is the integrity of your nerve system, which controls and regulates every cell and tissue of your body. The moving bones of the spinal column can impair this vital communication link between your brain and body. We help improve the function and structure of your spine, reducing nerve system compromise. The result?</p>
  <p class="highlight">Even non-spinal related health problems can show improvement</p>
  <ul class="benefits">
    <li><svg class="tick" viewBox="0 0 12 12"><circle cx="6" cy="6" r="6" fill="#7dbf3c"/><path d="M3.2 6.2l1.9 1.9 3.7-3.9" stroke="#fff" stroke-width="1.5" fill="none"/></svg>without drugs</li>
    <li><svg class="tick" viewBox="0 0 12 12"><circle cx="6" cy="6" r="6" fill="#7dbf3c"/><path d="M3.2 6.2l1.9 1.9 3.7-3.9" stroke="#fff" stroke-width="1.5" fill="none"/></svg>without surgery</li>
    <li><svg class="tick" viewBox="0 0 12 12"><circle cx="6" cy="6" r="6" fill="#7dbf3c"/><path d="M3.2 6.2l1.9 1.9 3.7-3.9" stroke="#fff" stroke-width="1.5" fill="none"/></svg>Regardless of age</li>
    <li><svg class="tick" viewBox="0 0 12 12"><circle cx="6" cy="6" r="6" fill="#7dbf3c"/><path d="M3.2 6.2l1.9 1.9 3.7-3.9" stroke="#fff" stroke-width="1.5" fill="none"/></svg>for over a century</li>
    <li><svg class="tick" viewBox="0 0 12 12"><circle cx="6" cy="6" r="6" fill="#7dbf3c"/><path d="M3.2 6.2l1.9 1.9 3.7-3.9" stroke="#fff" stroke-width="1.5" fill="none"/></svg>Naturally</li>
  </ul>
</section>

<section class="card card-front" aria-label="Card front">
  <div class="wordmark"><span class="dot"></span>Bright Path Wellness Centre</div>
  <div class="divider"></div>
  <address class="address">218 Farrow Gate<br>Etobicoke ON.<br>K2J 6P4</address>
  <div class="practitioner">
    <div class="name">Dr. Marten Quovel</div>
    <div class="creds">B.Sc., D.C.</div>
    <div class="title">Chiropractor</div>
  </div>
  <ul class="contacts">
    <li><svg viewBox="0 0 12 12"><path d="M2.5 1h2l1 3-1.4 1a6.5 6.5 0 0 0 2.9 2.9l1-1.4 3 1v2A1.5 1.5 0 0 1 9.5 11 8.5 8.5 0 0 1 1 2.5 1.5 1.5 0 0 1 2.5 1z"/></svg>416-872-0196 (PATH)</li>
    <li><svg viewBox="0 0 12 12"><path d="M1 2.5h10v7H1z"/><path d="M1 2.5l5 4 5-4" stroke="#fff" stroke-width=".9" fill="none"/></svg>brightpathchiro@mailbox.example</li>
    <li><svg viewBox="0 0 12 12"><circle cx="6" cy="6" r="5.5"/><path d="M.5 6h11M6 .5c-3 3-3 8 0 11M6 .5c3 3 3 8 0 11" stroke="#fff" stroke-width=".7" fill="none"/></svg>www.brightpathwellnesscentre.example</li>
  </ul>
</section>

</body>
</html>
```